Letterhead

We are looking for a basic letterhead. It should include our logo, website - northpeakkitchenware.com, phone 907.418.3952, toll free 855.392.6180, and fax 907.418.5263, along with our address 4837 Birchwood Lane, Anchorage, AK 99517. I want something that will look good printed in color or black and white.

```html
<!DOCTYPE html>
<html lang="en">
<head>
<meta charset="utf-8">
<title>North Peak Kitchenware – Letterhead</title>
<link href="https://fonts.googleapis.com/css2?family=Montserrat:wght@600;700;800&family=PT+Sans:wght@400;700&display=swap" rel="stylesheet">
<style>
  :root{
    --backdrop:#e6e7e9;
    --paper:#ffffff;
    --band-top:#0b6aa2;
    --band-deep:#17488a;
    --navy:#1d3a7a;
    --ink:#464646;
    --edge:#d9dde2;
  }
  html,body{margin:0;padding:0;width:1200px;height:900px;overflow:hidden;background:var(--backdrop);}
  .letterhead{
    position:absolute;left:336px;top:77px;width:528px;height:746px;
    background:var(--paper);overflow:hidden;
    font-family:"PT Sans",Arial,sans-serif;color:var(--ink);
  }
  .band{position:absolute;left:0;width:528px;}
  .band--top{top:0;height:112px;}
  .band--bottom{bottom:0;height:82px;}
  .brand-box{
    position:absolute;left:66px;top:27px;width:160px;height:81px;
    background:var(--paper);border-radius:8px 8px 0 0;
    display:flex;align-items:center;justify-content:center;
  }
  .brand-name{
    font-family:"Montserrat",Arial,sans-serif;font-weight:800;
    font-size:15px;line-height:1.1;color:var(--navy);text-align:center;
    letter-spacing:.3px;
  }
  .website{
    position:absolute;right:42px;top:30px;
    font-family:"Montserrat",Arial,sans-serif;font-weight:600;font-size:10.5px;
    color:#fff;letter-spacing:.2px;
  }
  .letter{
    position:absolute;left:55px;top:197px;width:422px;
    font-size:9.6px;line-height:12.7px;letter-spacing:-.1px;
  }
  .letter p{margin:0;}
  .recipient{margin-bottom:25px!important;}
  .salutation{margin-bottom:25px!important;}
  .body-copy{text-indent:32px;margin-bottom:12.7px!important;}
  .closing{margin-top:12px!important;}
  .signature{position:relative;height:44px;margin-top:4px;}
  .signature-mark{position:absolute;left:8px;top:2px;width:56px;height:34px;background:#d6d6d6;border-radius:4px;}
  .signature-line{position:absolute;left:0;top:33px;width:95px;border-top:1px dotted #555;}
  .contact{
    position:absolute;right:42px;top:647px;text-align:right;
    font-family:"Montserrat",Arial,sans-serif;font-weight:700;color:var(--navy);
  }
  .contact-address{font-size:10.5px;line-height:13px;}
  .contact-line{font-size:8.2px;line-height:10.5px;}
</style>
</head>
<body>
<main class="letterhead">
  <svg class="band band--top" viewBox="0 0 528 112" aria-hidden="true">
    <defs>
      <linearGradient id="bandTop" x1="0" y1="0" x2="0" y2="1">
        <stop offset="0" stop-color="var(--band-top)"/>
        <stop offset="1" stop-color="var(--band-deep)"/>
      </linearGradient>
    </defs>
    <path fill="var(--edge)" d="M0 0H528V104L520 99 508 106 496 98 480 101 468 94 452 97 440 90 424 94 410 88 396 93 382 86 366 90 352 84 336 88 322 81 306 86 290 79 276 84 262 76 246 81 232 74 226 80 210 78 190 84 170 76 150 82 130 76 110 80 90 74 70 79 50 73 34 78 18 72 0 76Z"/>
    <path fill="url(#bandTop)" d="M0 0H528V98L520 94 508 100 496 93 480 96 468 89 452 92 440 85 424 89 410 83 396 88 382 81 366 85 352 79 336 83 322 76 306 81 290 74 276 79 262 71 246 76 232 69 226 75 210 73 190 79 170 71 150 77 130 71 110 75 90 69 70 74 50 68 34 73 18 67 0 71Z"/>
  </svg>
  <div class="brand-box"><div class="brand-name">NORTH PEAK<br>KITCHENWARE</div></div>
  <div class="website">www. northpeakkitchenware.com</div>

  <section class="letter">
    <p class="recipient">13-02-2014<br>Nadun Wijesekara<br>Kelanigama Estate,<br>Rakwana<br>Sri lanka</p>
    <p class="salutation">Dear Sir,</p>
    <p class="body-copy">La rencontre était censée être un événement décisif pour le Nigeria alors que le pays a été classé comme la première économie africaine.Mais l'inquiétude est palpable dans la capitale après les récentes attaques menées par Boko Haram.Après une journée de rencontres privées, le forum</p>
    <p class="body-copy">Il est accompagné d'une importante délégation d'hommes d'affaires pour une tournée africaine.Au total, les organisateurs de l'événement s'attendent à la participation de plus de 70 pays d'Afrique. Toutefois, le forum a lieu dans une atmosphère dominée par les préoccupa­tions sécuritaires. La capitale Abuja a récemment été secouée par une double explosion qui a fait des dizaines de victimes. L'attentat a été attribué aux militants de Boko Haram qui ont revendiqué l'enlèvement de près de 200 lycéennes dans le nord du pays. Les organisateurs assurent qu'ils ont pris les mesures nécessaires pour assurer la sécurité des participants au foru</p>
    <p class="body-copy">Mais des investisseurs se disent prêt à ignorer certains risques sécuritaires à cause des opportunités commerciales que le Nigeria peut offrir notamment dans les secteurs comme le pétrole, le gaz et l'électricité.)revendiqué l'enlèvement de près de 200 ldfksffgl fglkfjglfkglfkjgfl jfkgjflkg jfgkfjl j flkjfg jlfkjgf ksld jlkgffk jglfkjjlf lkfdjlosdfl lfjlfkglf jdfldkjlfd lfd slgsdfnsdlkjflsdk-jflsdj dsfldskjf ycéennes dans le nord du pays. Les.</p>
    <p class="closing">Your Signature</p>
    <div class="signature">
      <div class="signature-mark" role="img" aria-label="Handwritten signature"></div>
      <div class="signature-line"></div>
    </div>
  </section>

  <address class="contact" style="font-style:normal">
    <div class="contact-address">4837 Birchwood Lane, Anchorage, AK 99517</div>
    <div class="contact-line">Phone : 907.418.3952 | Toll free : 855.392.6180</div>
    <div class="contact-line">Fax : 907.418.5263</div>
  </address>

  <svg class="band band--bottom" viewBox="0 0 528 82" aria-hidden="true">
    <path fill="var(--edge)" d="M0 4L14 0 28 8 44 3 60 10 76 5 92 12 110 7 126 14 142 9 160 16 178 11 196 18 214 13 232 20 250 15 268 22 286 17 304 24 322 19 340 26 358 21 376 28 394 23 412 30 430 25 448 32 466 27 484 34 502 29 518 35 528 31V82H0Z"/>
    <path fill="var(--band-top)" d="M0 14L14 10 28 18 44 13 60 20 76 15 92 22 110 17 126 24 142 19 160 26 178 21 196 28 214 23 232 30 250 25 268 32 286 27 304 34 322 29 340 36 358 31 376 38 394 33 412 40 430 35 448 42 466 37 484 44 502 39 518 45 528 41V82H0Z"/>
  </svg>
</main>
</body>
</html>
```